Business Card Design Project

Design a business card for a new entity that is in the OTC (over-the-counter-derivative brokering business-Financial Services.
The card should be clean a professional looking. We encourage designers to think pro-actively, fresh and innovative, but also keep in mind that only 2 things are important. a)that the card look professional b)that it is somehow memorable.

We have a new logo which we will upload and will want the Trident symbol in the logo to be raised OR not have the symbol raised and plan on having the word " BROKERAGE SERVICES" raised that stands out and will look sharp.

Along with uploading the new logo which MUST be incorperated, I am also going to upload 3 different business cards of other businesses to use only as guild-lines since I think they are clean and professional looking BUT I encourage all to be pro-active and creative on their own.

Industry/Entity Type

Business

Requirements
Must have
• 1. MUST HAVE THE NEW LOGO WHICH WILL BE UPLOADED
2. MUST HAVE A VERSION SIMILAR TO THE 3 DIFFERENT BUSINESS CARDS I WILL UPLOAD, BUT EACH DESIGNER MUST ONLY THESE THIS FORMAT AS A BACK-UP AND BE CREATIVE ON THEIR OWN FIRST. ALSO WHEN LOOKING AT THE CARDS WHICH I UPLOAD TO USE AS A GUILD-LINE KEEP IN MIND THAT THESE ARE KESTRAVEL 300 COMPANIES SO DO NOT MIMIC ONLY USE FOR IDEAS.
Nice to have
• these are the 3 different other biz cards to look at for some reference

```html
<!DOCTYPE html>
<html lang="en">
<head>
<meta charset="utf-8">
<title>Halvern Brokerage Services – Business Card</title>
<link rel="stylesheet" href="https://fonts.googleapis.com/css2?family=Open+Sans:wght@400;600&display=swap">
<style>
  :root {
    --page: #ffffff;
    --card-dark: #333333;
    --card-light: #ffffff;
    --silver: #d4d4d4;
    --ink: #3d3d3d;
    --ink-soft: #4a4a4a;
    --gold: #c9a227;
    --band-grey: #6b6b6b;
    --shadow: 0 4px 7px rgba(0, 0, 0, 0.35);
  }
  * { margin: 0; padding: 0; box-sizing: border-box; }
  html, body {
    width: 1200px;
    height: 901px;
    overflow: hidden;
    background: var(--page);
    font-family: "Open Sans", Arial, sans-serif;
  }
  .canvas { position: relative; width: 1200px; height: 901px; }

  .card {
    position: absolute;
    left: 279px;
    width: 644px;
    height: 368px;
    box-shadow: var(--shadow);
    overflow: hidden;
  }

  /* Front */
  .card--front { top: 49px; background: var(--card-dark); }
  .brand { position: absolute; left: 0; width: 100%; text-align: center; }
  .brand__mark {
    display: block;
    margin: 0 auto;
    border-radius: 50%;
  }
  .card--front .brand { top: 88px; color: var(--silver); }
  .card--front .brand__mark { width: 86px; height: 86px; background: var(--silver); margin-bottom: 34px; }
  .brand__name {
    display: block;
    font-weight: 600;
    letter-spacing: 2px;
    line-height: 1;
  }
  .brand__tag {
    display: block;
    font-weight: 600;
    letter-spacing: 4px;
    line-height: 1;
  }
  .card--front .brand__name { font-size: 44px; }
  .card--front .brand__tag { font-size: 15px; margin-top: 6px; }
  .front__web {
    position: absolute;
    top: 325px;
    width: 100%;
    text-align: center;
    color: #ffffff;
    font-size: 15px;
  }

  /* Back */
  .card--back { top: 484px; height: 367px; background: var(--card-light); }
  .card--back .brand { left: 38px; width: 260px; top: 52px; color: var(--ink); }
  .card--back .brand__mark { width: 76px; height: 76px; background: var(--ink); margin-bottom: 30px; }
  .card--back .brand__name { font-size: 40px; }
  .card--back .brand__tag { font-size: 13px; margin-top: 5px; }

  .person { position: absolute; left: 38px; width: 260px; top: 256px; text-align: center; }
  .person__name { color: var(--gold); font-size: 24px; font-weight: 600; line-height: 1.2; }
  .person__role { color: var(--ink-soft); font-size: 15px; line-height: 1.4; }

  .contact {
    position: absolute;
    left: 359px;
    top: 202px;
    list-style: none;
    color: var(--ink);
    font-size: 15px;
    line-height: 21.5px;
  }
  .contact__item { display: flex; align-items: center; gap: 6px; }
  .contact__icon { width: 13px; height: 13px; fill: var(--gold); flex: none; }

  .band { position: absolute; left: 0; bottom: 0; width: 100%; height: 21px; background: var(--band-grey); }
  .band__accent { position: absolute; left: 32px; top: 0; width: 276px; height: 100%; background: var(--gold); }
</style>
</head>
<body>
<main class="canvas">

  <section class="card card--front" aria-label="Card front">
    <div class="brand">
      <span class="brand__mark" aria-hidden="true"></span>
      <span class="brand__name">HALVERN</span>
      <span class="brand__tag">BROKERAGE SERVICES</span>
    </div>
    <p class="front__web">www.halvernbrokerage.com</p>
  </section>

  <section class="card card--back" aria-label="Card back">
    <div class="brand">
      <span class="brand__mark" aria-hidden="true"></span>
      <span class="brand__name">HALVERN</span>
      <span class="brand__tag">BROKERAGE SERVICES</span>
    </div>

    <div class="person">
      <p class="person__name">Daniel Pryce</p>
      <p class="person__role">Principal Consultant</p>
    </div>

    <ul class="contact">
      <li class="contact__item">1187 Corwin Lane #204</li>
      <li class="contact__item">Lakemoor, FL 32000</li>
      <li class="contact__item">
        <svg class="contact__icon" viewBox="0 0 16 16" aria-hidden="true"><path d="M3.6 1.2l2.3 2.6-1.3 2c.9 2 2.5 3.6 4.5 4.5l2-1.3 2.6 2.3-1.2 2.2C7.2 14.9 1.1 8.8.9 3.4z"/></svg>
        +1 (000) 000 - 0000
      </li>
      <li class="contact__item">
        <svg class="contact__icon" viewBox="0 0 16 16" aria-hidden="true"><path d="M4.5 0h7c.8 0 1.5.7 1.5 1.5v13c0 .8-.7 1.5-1.5 1.5h-7C3.7 16 3 15.3 3 14.5v-13C3 .7 3.7 0 4.5 0zM5 2v10h6V2zm3 11a1 1 0 100 2 1 1 0 000-2z"/></svg>
        +1 (000) 000 - 0000
      </li>
      <li class="contact__item">
        <svg class="contact__icon" viewBox="0 0 16 16" aria-hidden="true"><path d="M1 3h14v1.2L8 9 1 4.2zm0 2.6l7 4.8 7-4.8V13H1z"/></svg>
        dpryce@halvernbrokerage.com
      </li>
      <li class="contact__item">
        <svg class="contact__icon" viewBox="0 0 16 16" aria-hidden="true"><path d="M8 0a8 8 0 100 16A8 8 0 008 0zm5.9 7h-2.5a12 12 0 00-1-4.8A6 6 0 0113.9 7zM8 2c.8 1 1.3 2.8 1.4 5H6.6C6.7 4.8 7.2 3 8 2zM5.6 2.2a12 12 0 00-1 4.8H2.1a6 6 0 013.5-4.8zM2.1 9h2.5a12 12 0 001 4.8A6 6 0 012.1 9zM8 14c-.8-1-1.3-2.8-1.4-5h2.8c-.1 2.2-.6 4-1.4 5zm2.4-.2a12 12 0 001-4.8h2.5a6 6 0 01-3.5 4.8z"/></svg>
        www.halvernbrokerage.com
      </li>
    </ul>

    <div class="band" aria-hidden="true"><span class="band__accent"></span></div>
  </section>

</main>
</body>
</html>
```